Triathlon coaching company website design

A website is needed for a coaching company called StrideVantage. The company provides coaching services to triathletes and other endurance athletes. This includes 1:1 coaching, individualized training plan development, race preparation, and access to guidance and advice on all aspects of developing and maintaining a healthy lifestyle. The design should appeal to all levels of athletes, but be professional in appearance. The tone of the site should be in keeping with the company tagline: Endurance. Resilience. Achievement.

Target Market(s)

All levels of triathletes - beginners to professionals

Industry/Entity Type

It Company

Coding

Coded - Design and coding required

Number of Pages Required

1 page

Colors

Designer to choose colors to be used in the design.

Requirements
Must have
• Pages that should be included must cover: Introductory (Home), description in detail of what we do, description of the main coach (bio) and others types of expert advisors who can be available, link to contact the company, race reports for coaches and athletes that can be regularly updated, links to other sites of potential interest (e.g. other triathlon sites or my facebook page), twitter feed, sign up for email updates. Ability to add other links and pages in future months (e.g. shared calendar access to book meetings, credit card functionality, testimonials)
Should not have
• Not loud or down market feel - target market will largely be highly educated and reasonably affluent

```html
<!DOCTYPE html>
<html lang="en">
<head>
<meta charset="utf-8">
<title>StrideVantage – Endurance. Resilience. Achievement.</title>
<link href="https://fonts.googleapis.com/css2?family=Nunito:wght@400;600;700&family=Raleway:wght@400;500;600;700&display=swap" rel="stylesheet">
<style>
:root{
  --red:#a61f23;
  --dark:#2b2b2b;
  --footer:#252525;
  --ink:#3a3a3a;
  --muted:#666;
  --white:#fff;
}
*{margin:0;padding:0;box-sizing:border-box}
html,body{width:835px;height:1200px;overflow:hidden;background:var(--white)}
body{position:relative;font-family:"Raleway",sans-serif;color:var(--ink)}
.abs{position:absolute}

.topbar{left:0;top:0;width:835px;height:26px;background:var(--dark)}
.social{left:46px;top:0;display:flex;height:26px}
.social span{width:23px;height:26px;border-left:1px solid #444;display:flex;align-items:center;justify-content:center}
.social span:last-child{border-right:1px solid #444}
.social span i{width:6px;height:6px;background:#bbb;display:block}
.search{left:756px;top:0;width:24px;height:26px;border-left:1px solid #444;border-right:1px solid #444;display:flex;align-items:center;justify-content:center}

.header{left:0;top:26px;width:835px;height:56px;background:var(--white)}
.brand{left:46px;top:29px}
.brand-name{font-family:"Nunito",sans-serif;font-weight:700;font-size:24px;color:var(--red);display:flex;align-items:center;gap:6px;line-height:1}
.brand-name i{width:10px;height:10px;border-radius:50%;background:var(--red);display:block}
.brand-tag{font-family:"Nunito",sans-serif;font-size:7px;color:#222;letter-spacing:.2px;margin-top:7px}
.nav{left:453px;top:48px;display:flex;gap:19px;font-size:9.5px;letter-spacing:1.2px;font-weight:500;color:#333}
.nav a{color:inherit;text-decoration:none}
.nav a.active{color:var(--red)}
.cart{left:764px;top:44px}
.cart-count{left:778px;top:37px;width:9px;height:10px;background:var(--red);color:#fff;font-size:6px;text-align:center;line-height:10px;border-radius:2px}

.hero{left:0;top:82px;width:835px;height:305px;background:linear-gradient(100deg,#4d4944 0%,#6f6860 35%,#5a5a62 55%,#7c7468 75%,#5e5850 100%)}
.hero-caption{left:62px;top:262px;width:315px;height:79px;background:rgba(40,40,40,.55);padding:12px 10px;color:#fff}
.hero-caption h2{font-family:"Nunito",sans-serif;font-weight:400;font-size:15.5px;margin-bottom:4px}
.hero-caption p{font-family:"Nunito",sans-serif;font-size:10.5px;line-height:19px}

.promo{left:46px;top:469px;width:232px;height:201px;background:linear-gradient(160deg,#3d5a7a,#9fb4c8 50%,#2c3a4a)}
.welcome{left:297px;top:469px;width:485px}
.welcome h1{font-family:"Nunito",sans-serif;font-weight:600;font-size:22px;color:#333;border-left:2px solid var(--red);padding-left:13px;line-height:22px}
.welcome h3{font-family:"Nunito",sans-serif;font-weight:600;font-size:14.5px;color:var(--red);line-height:21px;margin-top:12px}
.welcome p{font-size:10.6px;line-height:24.5px;color:var(--muted);margin-top:7px}
.btn-read{display:inline-block;margin-top:17px;width:128px;height:32px;background:var(--red);color:#fff;font-size:7.5px;font-weight:700;letter-spacing:2.2px;text-align:center;line-height:32px}

.footer{left:0;top:755px;width:835px;height:445px;background:var(--footer);color:#fff;font-family:"Nunito",sans-serif}
.footer h4{position:absolute;left:46px;top:45px;font-size:13px;font-weight:600}
.label{position:absolute;font-size:9.5px;font-weight:600}
.label b{color:var(--red);font-weight:600}
.field{position:absolute;height:23px;background:#fff;border:1px solid var(--red)}
.sub{position:absolute;font-size:5.5px;font-weight:600}
.btn-send{position:absolute;left:46px;top:306px;width:151px;height:36px;background:#fff;color:var(--red);font-size:9.5px;font-weight:700;text-align:center;line-height:36px;border:1px solid #ddd}
.copy{position:absolute;left:0;width:835px;top:420px;text-align:center;font-size:5.5px;color:#888;font-weight:700;letter-spacing:.2px}
</style>
</head>
<body>
<div class="abs topbar"></div>
<div class="abs social"><span><i></i></span><span><i></i></span><span><i></i></span><span><i></i></span><span><i></i></span></div>
<div class="abs search"><svg width="8" height="8" viewBox="0 0 10 10"><circle cx="4" cy="4" r="3" fill="none" stroke="#bbb" stroke-width="1.2"/><line x1="6.3" y1="6.3" x2="9" y2="9" stroke="#bbb" stroke-width="1.2"/></svg></div>

<div class="abs header"></div>
<div class="abs brand">
  <div class="brand-name"><i></i>StrideVantage</div>
  <div class="brand-tag">ENDURANCE. RESILIENCE. ACHIEVEMENT</div>
</div>
<nav class="abs nav"><a class="active">HOME</a><a>SERVICES</a><a>NEWS</a><a>ABOUT</a><a>CONTACT US</a></nav>
<svg class="abs cart" width="14" height="15" viewBox="0 0 14 15"><path d="M1.5 5h11v9h-11z" fill="none" stroke="#333" stroke-width="1.2"/><path d="M4.5 5V3.5a2.5 2.5 0 0 1 5 0V5" fill="none" stroke="#333" stroke-width="1.2"/></svg>
<div class="abs cart-count">0</div>

<div class="abs hero" role="img" aria-label="Triathlon collage: open-water swimmer, cyclist in helmet, runner on a seaside boardwalk"></div>
<div class="abs hero-caption">
  <h2>Daniel Ashcombe</h2>
  <p>Triathlon &amp; Endurance Coach. Helping people build endurance, resilience and delight in personal achievement.</p>
</div>

<div class="abs promo" role="img" aria-label="Promotional photo of a cycling group inviting athletes to become a training ambassador"></div>
<section class="abs welcome">
  <h1>Welcome to StrideVantage</h1>
  <h3>Endurance, Resilience, Achievement are the watch-words of the StrideVantage brand.</h3>
  <p>At StrideVantage we believe that everyone has a unique set of circumstances, motivations and abilities that need to be taken into consideration in developing their program. Defining success is personal, as is the path to achieving that success.</p>
  <span class="btn-read">READ MORE</span>
</section>

<footer class="abs footer">
  <h4>Contact Us</h4>
  <div class="label" style="left:46px;top:83px">Name <b>*</b></div>
  <div class="field" style="left:46px;top:93px;width:352px"></div>
  <div class="field" style="left:428px;top:93px;width:351px"></div>
  <div class="sub" style="left:46px;top:120px">First</div>
  <div class="sub" style="left:428px;top:120px">Last</div>
  <div class="label" style="left:46px;top:146px">Email <b>*</b></div>
  <div class="field" style="left:46px;top:156px;width:352px"></div>
  <div class="field" style="left:428px;top:156px;width:351px"></div>
  <div class="sub" style="left:46px;top:183px">Email</div>
  <div class="sub" style="left:428px;top:183px">Confirm Email</div>
  <div class="label" style="left:46px;top:208px">Comment or Message <b>*</b></div>
  <div class="field" style="left:46px;top:218px;width:733px;height:75px"></div>
  <div class="btn-send">Contact StrideVantage Now!</div>
  <div class="copy">COPYRIGHT 2015 - ALL RIGHTS RESERVED.</div>
</footer>
</body>
</html>
```